Marlowe Solutions Business Card

We need a business card design for a software and IT consulting company called marlowe solutions. We would like to feature a kinkajou (it is a small tree-dwelling animal) somewhere in the design. We would like a green color involved somewhere (but not overwhelming). Back of card should be predominately a color, front of the card can be predominately white or predominately a different color than the back.

Information on front of card:

Contact information:
Phone: (555) 214-3907
Email: peter.dunmore@mrlsol.example
Website: www.mrlsol.example

Name: Peter Dunmore
Title: Owner / Developer

Information on back of card:
Marlowe Solutions
Targeted Solutions. Fit to your environment.

Industry/Entity Type

Software

Requirements
Should not have
• Avoid anything that too closely resembles a cartoon or campy feel. This should be professional and modern looking.

```html
<!DOCTYPE html>
<html lang="en">
<head>
<meta charset="utf-8">
<title>Marlowe Solutions Business Card</title>
<link rel="stylesheet" href="https://fonts.googleapis.com/css2?family=Lato:wght@400;700&family=Jost:wght@400&family=Arimo:wght@400&display=swap">
<style>
  :root {
    --backdrop: #8a5a30;
    --card-white: #ffffff;
    --card-dark: #231f20;
    --brand-grey: #8c8c8c;
    --ink: #231f20;
    --accent-green: #6db33f;
    --light-text: #ffffff;
    --animal-main: #a88a55;
    --animal-shade: #6f5530;
  }
  * { box-sizing: border-box; margin: 0; padding: 0; }
  html, body {
    width: 1070px;
    height: 1200px;
    overflow: hidden;
    background: var(--backdrop);
  }
  .card {
    position: absolute;
    left: 83px;
    width: 877px;
    height: 499px;
    border-radius: 34px;
    overflow: hidden;
  }
  .card-front { top: 70px; background: var(--card-white); }
  .card-back  { top: 602px; background: var(--card-dark); color: var(--light-text); text-align: center; }

  .front-brand {
    position: absolute;
    left: 47px;
    top: 42px;
    font-family: "Lato", sans-serif;
    font-weight: 400;
    font-size: 46px;
    color: var(--brand-grey);
    letter-spacing: -0.5px;
  }
  .holder {
    position: absolute;
    left: 47px;
    top: 158px;
    font-family: "Jost", sans-serif;
    color: var(--ink);
  }
  .holder-name { font-size: 29px; letter-spacing: 0.5px; }
  .holder-title { font-size: 22px; }

  .contact-list {
    position: absolute;
    left: 47px;
    top: 222px;
    list-style: none;
    font-family: "Jost", sans-serif;
    font-size: 22px;
    color: var(--ink);
  }
  .contact-item { display: flex; align-items: center; height: 30px; margin-bottom: 12px; }
  .contact-item.location { margin-top: 26px; }
  .contact-icon { width: 20px; height: 20px; margin-right: 10px; fill: var(--accent-green); flex: none; }

  .animal-photo {
    position: absolute;
    left: 616px;
    top: 254px;
    width: 208px;
    height: 183px;
    border-radius: 40% 45% 30% 35%;
    background: radial-gradient(circle at 40% 40%, var(--animal-main), var(--animal-shade));
  }

  .front-wave { position: absolute; left: 0; bottom: 0; width: 877px; height: 110px; }

  .front-web {
    position: absolute;
    left: 47px;
    top: 440px;
    font-family: "Jost", sans-serif;
    font-size: 21px;
    letter-spacing: 2px;
    color: var(--light-text);
  }

  .back-brand {
    position: absolute;
    left: 0; right: 0;
    top: 96px;
    font-family: "Lato", sans-serif;
    font-weight: 400;
    font-size: 60px;
    letter-spacing: -0.5px;
  }
  .back-tagline {
    position: absolute;
    left: 0; right: 0;
    top: 228px;
    font-family: "Arimo", sans-serif;
    font-size: 42px;
    line-height: 61px;
  }
  .back-web {
    position: absolute;
    left: 0; right: 0;
    top: 398px;
    font-family: "Arimo", sans-serif;
    font-size: 27px;
    letter-spacing: 2px;
  }
</style>
</head>
<body>
  <section class="card card-front">
    <div class="front-brand">MARLOWE SOLUTIONS</div>
    <div class="holder">
      <span class="holder-name">PETER DUNMORE,</span>
      <span class="holder-title">Owner / Developer</span>
    </div>
    <ul class="contact-list">
      <li class="contact-item">
        <svg class="contact-icon" viewBox="0 0 20 20"><path d="M6 2c1 0 2 3 2 4s-2 1.5-2 2.5 2.5 4.5 4 5.5c1 0 1.5-2 2.5-2s3.5 1.5 3.5 2.5-2 3.5-4 3.5C7 18 2 12 2 6c0-2 3-4 4-4z"/></svg>
        (555) 214-3907
      </li>
      <li class="contact-item">
        <svg class="contact-icon" viewBox="0 0 20 20"><path d="M2 8l8-5 8 5v9H2z"/><path d="M3.5 9l6.5 4 6.5-4" fill="none" stroke="#fff" stroke-width="1.4"/></svg>
        peter.dunmore@mrlsol.example
      </li>
      <li class="contact-item location">
        <svg class="contact-icon" viewBox="0 0 20 20"><path d="M10 1a6.5 6.5 0 0 1 6.5 6.5C16.5 12 10 19 10 19S3.5 12 3.5 7.5A6.5 6.5 0 0 1 10 1zm0 4a2.5 2.5 0 1 0 0 5 2.5 2.5 0 0 0 0-5z" fill-rule="evenodd"/></svg>
        Fairview, TX
      </li>
    </ul>
    <div class="animal-photo" role="img" aria-label="Photograph of a kinkajou walking on a branch"></div>
    <svg class="front-wave" viewBox="0 0 877 110" preserveAspectRatio="none">
      <path d="M0 26 C 200 50, 330 70, 500 58 C 650 46, 780 18, 877 4 L877 110 L0 110 Z" fill="var(--card-dark)"/>
      <path d="M0 18 C 200 40, 330 60, 500 50 C 650 40, 780 12, 877 0 L877 4 C 780 18, 650 46, 500 58 C 330 70, 200 50, 0 26 Z" fill="var(--accent-green)"/>
    </svg>
    <div class="front-web">www.mrlsol.example</div>
  </section>

  <section class="card card-back">
    <div class="back-brand">MARLOWE SOLUTIONS</div>
    <div class="back-tagline">TARGETED SOLUTIONS<br>FIT TO YOUR ENVIRONMENT.</div>
    <div class="back-web">www.mrlsol.example</div>
  </section>
</body>
</html>
```